Personal Training Studio Checkin App (or URL based)

I would like a simple web based app built for our  business. We have a training studio with a simple business model. All our clients buy sessions in packages either 4, 8, or 12 at a time. We want something that a trainer can pull up and Check in a client. This will record the date and time the client was checked in, by what trainer, and what type of session. This system will keep track of the following:
Whenever a Client Checks in so it will ‘tick off’ a session on their package (ie- they have gone from 11 sessions left to 10 sessions left)
Track what sessions a particular trainer does so we can pay them at the end of the week and look at who they trained, what type of session and how many
Look at client activity: Every time they check in, Recharge their package, any activity related to the client, even if it was admin – like deleting a session that was mistakenly recorded.
This will keep a database of clients added and all their activity
The pdf I have included lays out how I think it would work and the features I want
I would like this to run off an tablora that we have at our front check in counter. It can be an app or a URL that use.
***THIS PROJECT IS NOT SO MUCH ABOUT DESIGN BUT ABOUT FUNCTIONALITY OF THE APPLICATION. IT MUST HAVE THE FEATURES I HAVE ASKED FOR THAT WORK TOGETHER. I AM WILLING TO PAY A LITTLE MORE AS A BONUS IF YOU CAN ACCOMPLISH THIS. ALSO IF I FIN THE RIGHT PERSON THAT CAN DO THIS I WILL MAKE IT A GUARNTEED PROJECT.

- Functionality and Track and record all the info we need

```html
<!DOCTYPE html>
<html lang="en">
<head>
<meta charset="utf-8">
<title>Client Check-In</title>
<link rel="stylesheet" href="https://fonts.googleapis.com/css2?family=Noto+Sans:wght@400;500&display=swap">
<style>
  :root {
    --ink: #212529;
    --muted: #6c757d;
    --line: #dee2e6;
    --card: #ffffff;
    --primary: #0d6efd;
    --on-dark: #ffffff;
    --gym-dark: #1c1c1e;
    --gym-mid: #3a3a3d;
    --gym-light: #8a8a8e;
  }
  * { box-sizing: border-box; margin: 0; padding: 0; }
  html, body { width: 1200px; height: 888px; overflow: hidden; }
  body {
    position: relative;
    font-family: "Noto Sans", sans-serif;
    color: var(--ink);
    background: var(--gym-dark);
  }
  .backdrop {
    position: absolute; inset: 0;
    background:
      radial-gradient(ellipse at 85% 10%, var(--gym-light) 0%, transparent 45%),
      radial-gradient(ellipse at 10% 5%, #6e6e72 0%, transparent 40%),
      linear-gradient(180deg, var(--gym-mid) 0%, #2a2a2c 45%, var(--gym-dark) 100%);
  }
  .checkin-card {
    position: absolute;
    left: 329px; top: 45px;
    width: 556px; height: 416px;
    background: var(--card);
    border-radius: 5px;
  }
  .card-title {
    position: absolute; left: 0; right: 0; top: 25px;
    height: 32px; line-height: 32px;
    text-align: center;
    font-size: 28px; font-weight: 500;
  }
  .field-label {
    position: absolute; left: 22px;
    height: 16px; line-height: 16px;
    font-size: 14px;
  }
  .field {
    position: absolute; left: 22px; width: 512px; height: 35px;
    border: 1px solid var(--line);
    border-radius: 5px;
    font-size: 14px;
    padding: 0 12px;
    display: flex; align-items: center; justify-content: space-between;
  }
  .field svg { width: 12px; height: 12px; }
  .btn {
    position: absolute; left: 22px; width: 512px; height: 35px;
    border-radius: 5px;
    color: var(--on-dark);
    font-size: 14px;
    display: flex; align-items: center; justify-content: center;
  }
  .btn-primary { background: var(--primary); }
  .btn-secondary { background: var(--muted); }
  .client-label { top: 129px; }
  .client-field { top: 109px; }
  .trainer-label { top: 162px; }
  .trainer-field { top: 188px; }
  .session-label { top: 241px; }
  .session-field { top: 268px; }
  .checkin-btn { top: 317px; }
  .home-btn { top: 360px; }
</style>
</head>
<body>
  <div class="backdrop" role="img" aria-label="Photo of a trainer guiding a client through a barbell squat in a dimly lit gym"></div>

  <form class="checkin-card">
    <h1 class="card-title">Client Check-In</h1>

    <label class="field-label" style="top:83px">Client Name</label>
    <div class="field client-field"></div>

    <label class="field-label trainer-label">Trainer Name</label>
    <div class="field trainer-field">
      <span>Select Trainer</span>
      <svg viewBox="0 0 16 16" aria-hidden="true"><path d="M2 5l6 6 6-6" fill="none" stroke="#343a40" stroke-width="2" stroke-linecap="round" stroke-linejoin="round"/></svg>
    </div>

    <label class="field-label session-label">Session Type</label>
    <div class="field session-field">
      <span>Select Session Type</span>
      <svg viewBox="0 0 16 16" aria-hidden="true"><path d="M2 5l6 6 6-6" fill="none" stroke="#343a40" stroke-width="2" stroke-linecap="round" stroke-linejoin="round"/></svg>
    </div>

    <div class="btn btn-primary checkin-btn">Check In</div>
    <div class="btn btn-secondary home-btn">Back to Home</div>
  </form>
</body>
</html>
```